Looking for a professional, clean and crisp business card

I am in the underground utilities industry and am just looking for a really impressive business card. I would like our card to be white with our symbol crisp and clear with it protruding. I also have a business partner that will require his name and info on the card once the design is set. I would like to have our website info on the card which is;
http://harbortrenchco.example/

Contact Information for Business Card

Website, contact name, number and email

```html
<!DOCTYPE html>
<html lang="en">
<head>
<meta charset="utf-8">
<title>Harbor Trench Co — Business Card</title>
<link href="https://fonts.googleapis.com/css2?family=Roboto+Condensed:wght@400;700&display=swap" rel="stylesheet">
<style>
  :root {
    --backdrop: #e6e7e9;
    --card: #ffffff;
    --ink: #1b1b1b;
    --accent: #3d64ad;
    --rule: #9a9a9a;
    --ghost: #efedeb;
    --shadow: rgba(0,0,0,0.14);
  }
  html, body {
    margin: 0;
    padding: 0;
    width: 1200px;
    height: 900px;
    overflow: hidden;
    background: var(--backdrop);
    font-family: "Roboto Condensed", Arial, sans-serif;
  }
  .canvas {
    position: relative;
    width: 1200px;
    height: 900px;
  }
  .card {
    position: absolute;
    width: 620px;
    height: 354px;
    background: var(--card);
    box-shadow: 0 14px 30px var(--shadow), 0 2px 4px rgba(0,0,0,0.08);
    overflow: hidden;
  }
  .card--front { left: 70px; top: 70px; }
  .card--back { left: 510px; top: 476px; }

  .ghost-mark {
    position: absolute;
    right: -40px;
    top: 28px;
    width: 380px;
    height: 380px;
    border-radius: 50%;
    border: 22px solid var(--ghost);
    box-sizing: border-box;
  }
  .ghost-name {
    position: absolute;
    right: -10px;
    top: 118px;
    width: 340px;
    text-align: center;
    font-weight: 700;
    font-size: 56px;
    line-height: 1;
    letter-spacing: 1px;
    text-transform: uppercase;
    color: var(--ghost);
  }

  .brand {
    position: absolute;
    display: flex;
    align-items: center;
    gap: 12px;
  }
  .brand__dot {
    width: 26px;
    height: 26px;
    border-radius: 50%;
    background: var(--ink);
    flex: none;
  }
  .brand__name {
    font-weight: 700;
    text-transform: uppercase;
    color: var(--ink);
    line-height: 1;
    letter-spacing: 0.5px;
  }
  .card--front .brand { left: 44px; top: 62px; }
  .card--front .brand__name { font-size: 30px; }
  .card--back .brand { left: 50%; top: 50%; transform: translate(-50%, -50%); gap: 16px; }
  .card--back .brand__dot { width: 36px; height: 36px; }
  .card--back .brand__name { font-size: 44px; }

  .divider {
    position: absolute;
    left: 44px;
    right: 44px;
    top: 150px;
    height: 1px;
    background: var(--rule);
  }

  .person {
    position: absolute;
    left: 44px;
    top: 190px;
    right: 44px;
  }
  .person__name {
    margin: 0;
    font-weight: 700;
    font-size: 22px;
    letter-spacing: 0.5px;
    text-transform: uppercase;
    color: var(--ink);
  }
  .person__role {
    margin: 2px 0 0;
    font-weight: 700;
    font-size: 15px;
    letter-spacing: 0.5px;
    text-transform: uppercase;
    color: var(--accent);
  }

  .contacts {
    position: absolute;
    left: 44px;
    top: 256px;
    margin: 0;
    padding: 0;
    list-style: none;
  }
  .contacts__item {
    display: flex;
    align-items: center;
    gap: 12px;
    height: 26px;
    margin-bottom: 4px;
    font-size: 15px;
    letter-spacing: 0.6px;
    text-transform: uppercase;
    color: var(--ink);
  }
  .contacts__icon {
    width: 22px;
    height: 22px;
    background: var(--accent);
    display: flex;
    align-items: center;
    justify-content: center;
    flex: none;
  }
</style>
</head>
<body>
<main class="canvas">

  <section class="card card--front" aria-label="Business card, contact side">
    <div class="ghost-mark" aria-hidden="true"></div>
    <div class="ghost-name" aria-hidden="true">Harbor Trench Co</div>

    <div class="brand">
      <span class="brand__dot"></span>
      <span class="brand__name">Harbor Trench Co</span>
    </div>

    <div class="divider"></div>

    <div class="person">
      <p class="person__name">Dale Merrow</p>
      <p class="person__role">Owner</p>
    </div>

    <ul class="contacts">
      <li class="contacts__item">
        <span class="contacts__icon">
          <svg width="14" height="14" viewBox="0 0 24 24" aria-hidden="true"><path fill="#fff" d="M6.6 10.8c1.4 2.8 3.8 5.1 6.6 6.6l2.2-2.2c.3-.3.7-.4 1-.2 1.1.4 2.3.6 3.6.6.6 0 1 .4 1 1V20c0 .6-.4 1-1 1C10.6 21 3 13.4 3 4c0-.6.4-1 1-1h3.5c.6 0 1 .4 1 1 0 1.3.2 2.5.6 3.6.1.3 0 .7-.2 1z"/></svg>
        </span>
        555-014-2286
      </li>
      <li class="contacts__item">
        <span class="contacts__icon">
          <svg width="14" height="14" viewBox="0 0 24 24" aria-hidden="true"><rect x="3" y="6" width="18" height="12" fill="#fff"/><path d="M3 6l9 7 9-7" fill="none" stroke="#3d64ad" stroke-width="1.8"/></svg>
        </span>
        dale@harbortrenchco.example
      </li>
      <li class="contacts__item">
        <span class="contacts__icon">
          <svg width="14" height="14" viewBox="0 0 24 24" aria-hidden="true"><g fill="none" stroke="#fff" stroke-width="1.8"><circle cx="12" cy="12" r="9"/><ellipse cx="12" cy="12" rx="4" ry="9"/><path d="M3 12h18M5 7h14M5 17h14"/></g></svg>
        </span>
        www.harbortrenchco.example
      </li>
    </ul>
  </section>

  <section class="card card--back" aria-label="Business card, brand side">
    <div class="brand">
      <span class="brand__dot"></span>
      <span class="brand__name">Harbor Trench Co</span>
    </div>
  </section>

</main>
</body>
</html>
```